Marlow Crest Group (Real Estate and Investment)

A high end, clean design.
We are a real estate company with sales, asset management and investment divisions. We want to use a black and white scheme which is really high end feel. The back of the card can just be the logo (black background with the white writing) as we will probably emboss this when we print)

Target Market(s)

High level investors, high end houses for sale

Industry/Entity Type

Business

Contact Information for Business Card

Name, position, phone number and email address
Glen Varley, Managing Director, 0437259064 and glen@marlowcrest-example.com.au

Requirements
Must have
• Back of the card to be the black background with the white writing (as per the attached images). Would like the capacity to emboss the writing and logo

```html
<!DOCTYPE html>
<html lang="en">
<head>
<meta charset="utf-8">
<title>Marlow Crest Group – Business Card</title>
<link rel="stylesheet" href="https://fonts.googleapis.com/css2?family=Lato:wght@300;400;700&family=Raleway:wght@300&display=swap">
<style>
  :root {
    --backdrop: #2e2826;
    --card-white: #ffffff;
    --card-black: #050505;
    --ink: #1a1a1a;
    --ink-soft: #3a3a3a;
    --rule: #8a8a8a;
    --reverse-ink: #f2f2f2;
  }
  * { margin: 0; padding: 0; box-sizing: border-box; }
  html, body {
    width: 1200px;
    height: 780px;
    overflow: hidden;
    background: var(--backdrop);
  }
  .canvas {
    position: relative;
    width: 1200px;
    height: 780px;
  }
  .card {
    position: absolute;
    top: 247px;
    width: 500px;
    height: 286px;
    box-shadow: 0 12px 30px rgba(0,0,0,0.45);
  }
  /* Front */
  .card--front {
    left: 70px;
    background: var(--card-white);
    color: var(--ink);
    font-family: "Lato", sans-serif;
  }
  .front-strip {
    position: absolute;
    left: 34px;
    bottom: 34px;
    display: flex;
    align-items: center;
  }
  .brand-mark {
    display: flex;
    align-items: center;
    gap: 8px;
    margin-right: 16px;
  }
  .brand-mark__circle {
    width: 38px;
    height: 38px;
    border: 1.5px solid var(--ink);
    border-radius: 50%;
  }
  .brand-mark__name {
    font-family: "Lato", sans-serif;
    font-weight: 400;
    font-size: 8px;
    letter-spacing: 1px;
    line-height: 1.35;
    text-transform: uppercase;
    color: var(--ink);
  }
  .person__name {
    font-size: 17px;
    letter-spacing: 0.5px;
    line-height: 1;
    text-transform: uppercase;
  }
  .person__name .given { font-weight: 300; }
  .person__name .family { font-weight: 700; }
  .person__title {
    margin-top: 4px;
    font-size: 9px;
    font-weight: 400;
    letter-spacing: 0.8px;
    text-transform: uppercase;
    color: var(--ink-soft);
  }
  .divider {
    width: 1px;
    height: 36px;
    background: var(--rule);
    margin: 0 16px;
  }
  .contact {
    font-size: 12px;
    line-height: 1.55;
    color: var(--ink);
  }
  /* Back */
  .card--back {
    left: 630px;
    background: var(--card-black);
    color: var(--reverse-ink);
    display: flex;
    flex-direction: column;
    align-items: center;
    justify-content: center;
    gap: 22px;
  }
  .back-mark {
    width: 78px;
    height: 78px;
    border: 1.5px solid var(--reverse-ink);
    border-radius: 50%;
  }
  .back-name {
    font-family: "Raleway", sans-serif;
    font-weight: 300;
    font-size: 22px;
    letter-spacing: 0.5px;
    text-transform: uppercase;
  }
</style>
</head>
<body>
<main class="canvas">
  <section class="card card--front" aria-label="Business card front">
    <div class="front-strip">
      <div class="brand-mark">
        <span class="brand-mark__circle"></span>
        <span class="brand-mark__name">Marlow<br>Crest Group</span>
      </div>
      <div class="person">
        <p class="person__name"><span class="given">Glen</span> <span class="family">Varley</span></p>
        <p class="person__title">Managing Director</p>
      </div>
      <span class="divider"></span>
      <div class="contact">
        <p>P: 043-725-9064</p>
        <p>E: glen@marlowcrest-example.com.au</p>
      </div>
    </div>
  </section>

  <section class="card card--back" aria-label="Business card back">
    <span class="back-mark"></span>
    <p class="back-name">Marlow Crest Group</p>
  </section>
</main>
</body>
</html>
```